App-Design für einen 24/7-Waren-Shop
Zielgruppe
App für einen 24/7-Waren-Shop, wo man über die App kaufen kann und im Shop nur noch die Ware abholt. Einmal sind es e Zigaretten und einmal Kontaktlinsen
Aufgabenstellung
Das Gesicht ist Vorgabe, sowie die Struktur die wir benötigen. Es soll hyper modern werden, damit die Kunden gerne auf die App gehen. In der Beilage ein Bild bzw. ein paar einfache Bilder, wie die App sein könnte....

```html
<!DOCTYPE html>
<html lang="de">
<head>
<meta charset="utf-8">
<title>Shop 24/7 Full UI Kit</title>
<link href="https://fonts.googleapis.com/css2?family=Inter:wght@400;500;600;700;800&display=swap" rel="stylesheet">
<style>
:root{
  --bg:#f3f4f6;
  --white:#ffffff;
  --ink:#141a2b;
  --navy:#141a2e;
  --muted:#8b93a1;
  --line:#e6e8ec;
  --soft:#f4f6f8;
  --blue:#16a0e6;
  --blue-soft:#e6f4fc;
  --yellow:#f7c81e;
  --green:#22b455;
  --green-soft:#dcf5e4;
  --red:#e5484d;
}
*{box-sizing:border-box;margin:0;padding:0}
html,body{width:1200px;height:2805px;overflow:hidden}
body{background:var(--bg);font-family:"Inter",sans-serif;color:var(--ink);position:relative}
svg.i{width:14px;height:14px;fill:none;stroke:currentColor;stroke-width:2;stroke-linecap:round;stroke-linejoin:round;flex:none}
.kit-title{position:absolute;top:40px;left:0;width:1200px;text-align:center;font-size:24px;font-weight:600;letter-spacing:-.3px}
.kit-sub{position:absolute;top:78px;left:0;width:1200px;text-align:center;font-size:12px;color:var(--muted);letter-spacing:.6px}
.label{position:absolute;width:270px;text-align:center;font-size:10.5px;font-weight:600;letter-spacing:1.2px;color:#a2a8b3}
.screen{position:absolute;width:270px;height:560px;background:var(--white);border-radius:34px;overflow:hidden;box-shadow:0 6px 24px rgba(20,26,46,.08);border:1px solid #e3e5ea}
.c1{left:30px}.c2{left:321px}.c3{left:612px}.c4{left:903px}
.r1{top:180px}.r2{top:853px}.r3{top:1526px}.r4{top:2199px}
.l1{top:148px}.l2{top:821px}.l3{top:1494px}.l4{top:2167px}
.hdr{height:84px;padding:50px 20px 0;display:flex;align-items:flex-start;gap:14px;font-size:12.5px;font-weight:800;letter-spacing:.2px;border-bottom:1px solid var(--line);background:var(--white)}
.hdr.center{justify-content:space-between}
.hdr.center .t{flex:1;text-align:center}
.body-gray{background:var(--soft);position:absolute;top:84px;left:0;right:0;bottom:0;padding:16px 14px}
.btn{display:flex;align-items:center;justify-content:center;gap:8px;height:40px;border-radius:8px;font-size:11.5px;font-weight:700;letter-spacing:.3px}
.btn.blue{background:var(--blue);color:#fff}
.btn.navy{background:var(--navy);color:#fff}
.btn.outline{border:1px solid var(--line);background:#fff;color:var(--ink);font-weight:600;font-size:10.5px}
.card{background:#fff;border:1px solid var(--line);border-radius:10px}
.ph{border-radius:8px;flex:none}
.home-logo{position:absolute;left:80px;top:48px;width:110px;height:110px;border-radius:50%;background:radial-gradient(circle at 40% 40%,#f0c12a 0,#8a6a12 45%,#17130a 75%);border:4px solid var(--yellow)}
.badge24{position:absolute;right:18px;top:32px;transform:rotate(10deg);border:1px solid var(--ink);border-radius:4px;background:#fff;font-size:8.5px;font-weight:800;padding:3px 6px}
.home-sheet{position:absolute;left:0;right:0;top:204px;bottom:0;background:linear-gradient(#fafbfc,#f1f3f5);border-radius:26px 26px 0 0;padding:22px 26px 0}
.handle{width:40px;height:3px;border-radius:2px;background:#dadde2;margin:0 auto}
.home-name{text-align:center;font-size:21px;font-weight:800;margin-top:16px;letter-spacing:-.3px}
.home-tag{text-align:center;font-size:8.5px;color:var(--muted);letter-spacing:1.3px;margin-top:3px}
.row-btn{display:flex;align-items:center;gap:10px;height:36px;border:1px solid var(--line);border-radius:7px;background:#fff;padding:0 12px;font-size:10px;font-weight:700;margin-top:9px;color:var(--ink)}
.row-btn .sp{flex:1}
.dot{width:5px;height:5px;border-radius:50%;background:var(--red)}
.home-foot{position:absolute;left:26px;right:26px;bottom:28px;display:flex;justify-content:space-between;font-size:8.5px;font-weight:700;color:var(--blue)}
.home-foot span:last-child{color:var(--muted);font-weight:500}
.login{padding:76px 26px 0;text-align:center}
.login-icon{width:54px;height:54px;border-radius:12px;background:var(--yellow);margin:0 auto;display:flex;align-items:center;justify-content:center;color:var(--ink)}
.login-icon svg{width:24px;height:24px}
.login h2{font-size:17px;font-weight:500;margin-top:22px}
.login p{font-size:10px;color:var(--muted);line-height:1.6;margin-top:10px}
.flabel{text-align:left;font-size:8px;font-weight:700;letter-spacing:.8px;color:#5b6270;margin:22px 0 8px}
.input{height:40px;border-radius:8px;background:var(--soft);display:flex;align-items:center;padding:0 12px;font-size:11px;color:#a3a9b4;justify-content:space-between}
.forgot{text-align:right;font-size:8px;color:var(--muted);margin:14px 0 12px}
.oder{display:flex;align-items:center;gap:10px;font-size:7.5px;color:#b5bac3;margin:22px 0 12px;letter-spacing:.6px}
.oder::before,.oder::after{content:"";flex:1;height:1px;background:var(--line)}
.item{display:flex;gap:10px;padding:8px;margin-bottom:10px}
.item .ph{width:66px;height:66px;background:radial-gradient(circle at 50% 50%,#e9894a 0,#c3431f 55%,#6b3a22 100%)}
.item .info{flex:1;position:relative;padding-top:3px}
.item .name{font-size:10px;font-weight:800}
.pts{position:absolute;right:0;top:2px;background:var(--yellow);font-size:7px;font-weight:800;padding:2px 4px;border-radius:3px}
.item .desc{font-size:7px;color:var(--muted);margin-top:5px;line-height:1.35;height:20px}
.item .bp{font-size:7.5px;color:var(--blue);font-weight:600;margin-top:6px}
.item .add{position:absolute;right:0;bottom:0;color:var(--blue)}
.item .add svg{width:15px;height:15px}
.news{display:flex;gap:12px;padding:14px 12px;margin-bottom:12px}
.nicon{width:38px;height:38px;border-radius:8px;display:flex;align-items:center;justify-content:center;flex:none}
.nicon svg{width:18px;height:18px}
.news h4{font-size:10px;font-weight:800}
.news p{font-size:7.5px;color:var(--muted);line-height:1.55;margin-top:5px}
.map{position:absolute;top:84px;left:0;right:0;height:330px;background:linear-gradient(160deg,#e4e7eb 0,#d7dbe0 50%,#e2e5e9 100%)}
.pill{position:absolute;background:#fff;border-radius:6px;font-size:8px;font-weight:700;padding:5px 9px;box-shadow:0 2px 6px rgba(0,0,0,.08);display:flex;align-items:center;gap:5px}
.map-pin{position:absolute;left:120px;top:240px;color:var(--red)}
.map-pin svg{width:26px;height:26px;stroke-width:2.2}
.loc-card{position:absolute;left:14px;right:14px;top:400px;background:#fff;border-radius:12px;padding:14px 14px 12px;box-shadow:0 6px 18px rgba(0,0,0,.08)}
.kv{display:flex;justify-content:space-between;font-size:8px;color:var(--muted);margin-bottom:13px}
.kv b{color:var(--ink);font-weight:700}
.kv .on{color:var(--green);font-weight:700}
.mrow{display:flex;align-items:center;gap:10px;height:44px;padding:0 20px;font-size:11.5px;font-weight:600}
.mrow .sp{flex:1}
.mrow svg.i{color:#8b93a1}
.mrow.active{background:var(--blue-soft)}
.mrow.active svg.i{color:var(--blue)}
.dbar{height:36px;background:var(--blue);color:#fff;display:flex;align-items:center;gap:8px;padding:0 12px;font-size:11.5px;font-weight:700}
.dbar .sp{flex:1}
.dopt{height:34px;border:1px solid var(--line);border-radius:6px;background:#fff;margin:7px 6px 0;display:flex;align-items:center;justify-content:space-between;padding:0 11px;font-size:10px;font-weight:700}
.dopt.sel{border-color:var(--blue);background:#f4faff}
.dopt.sel svg{color:var(--blue)}
.soft-btn{margin:28px 14px 0;height:34px;border-radius:7px;background:var(--blue-soft);border:1px solid #cfe8f7;color:var(--blue);font-size:10px;font-weight:700;display:flex;align-items:center;justify-content:center;letter-spacing:.3px}
.dark-top{background:var(--navy);color:#fff;border-radius:0 0 18px 18px;padding:44px 14px 14px}
.dark-top .row{display:flex;align-items:center;justify-content:space-between;font-size:12.5px;font-weight:800}
.select{margin-top:16px;height:30px;border-radius:6px;background:#2a3146;display:flex;align-items:center;gap:8px;padding:0 10px;font-size:9.5px;font-weight:700}
.select .sp{flex:1}
.select svg.y{color:var(--yellow)}
.prod{display:flex;gap:12px;padding:10px;margin:10px 10px 0;position:relative}
.prod .ph{width:40px;height:58px;background:linear-gradient(180deg,#f6f0dc 0,#e7a42a 30%,#b86a10 100%)}
.prod .nm{font-size:10px;font-weight:800;margin-top:10px}
.prod .sb{font-size:7px;color:var(--muted);margin-top:2px}
.prod .pr{font-size:10.5px;font-weight:700;margin-top:6px;display:flex;align-items:center;gap:8px}
.prod .pr i{font-style:normal;font-size:6.5px;color:#b5bac3;background:var(--soft);padding:1px 4px;border-radius:3px;font-weight:500}
.star{position:absolute;right:10px;top:10px;width:20px;height:20px;border:1px solid var(--line);border-radius:50%;display:flex;align-items:center;justify-content:center;color:#b5bac3}
.star svg{width:10px;height:10px}
.plus{position:absolute;right:10px;bottom:10px;width:22px;height:22px;border-radius:50%;background:var(--navy);color:#fff;display:flex;align-items:center;justify-content:center}
.plus svg{width:11px;height:11px;stroke-width:2.6}
.dt-top{height:84px;background:var(--navy)}
.dt-sheet{padding:14px 20px 0}
.dt-head{display:flex;gap:18px;margin-top:20px}
.dt-head .ph{width:72px;height:92px;background:linear-gradient(180deg,#f3ead1 0,#e5a226 35%,#a85c0c 100%);border:6px solid var(--soft)}
.dt-head h3{font-size:15px;font-weight:800;line-height:1.05;width:90px}
.dt-head .sb{font-size:9px;color:var(--muted);margin-top:4px}
.dt-head .nw{font-size:8px;color:var(--muted);text-decoration:underline;margin-top:6px}
.dt-head .pr{font-size:18px;font-weight:700;margin-top:12px}
.stepper{display:flex;align-items:center;justify-content:space-between;height:40px;border:1px solid var(--line);border-radius:8px;padding:0 4px;margin-top:28px;font-size:12px;font-weight:700}
.stepper span.b{width:32px;height:32px;border:1px solid var(--line);border-radius:6px;display:flex;align-items:center;justify-content:center}
.radio{width:12px;height:12px;border-radius:50%;border:1.5px solid #cdd1d8;flex:none}
.radio.on{border:3.5px solid var(--blue)}
.opt{display:flex;align-items:center;gap:12px;height:36px;border:1px solid var(--line);border-radius:8px;padding:0 12px;margin-top:8px;font-size:10px;font-weight:700}
.opt .sp{flex:1}
.opt.on{border-color:var(--blue);background:#f4faff}
.opt small{font-size:7.5px;color:var(--muted);font-weight:500}
.pay-top{background:var(--navy);color:#fff;border-radius:0 0 22px 22px;height:78px;padding:44px 20px 0;display:flex;gap:14px;font-size:12.5px;font-weight:800}
.pay-body{padding:24px 20px 0}
.pay-body h5{font-size:11.5px;font-weight:800;letter-spacing:.3px;margin-bottom:14px}
.popt{display:flex;align-items:center;gap:14px;height:46px;border:1px solid var(--line);border-radius:10px;padding:0 16px;margin-bottom:8px;font-size:10px;font-weight:700}
.popt .sp{flex:1}
.popt.on{border:1.5px solid var(--blue);background:#f2f9fe}
.free{font-size:7.5px;font-weight:800;color:var(--red);background:#fde8e8;padding:2px 5px;border-radius:3px}
.total{position:absolute;left:20px;right:20px;bottom:80px;border-top:1px solid var(--line);padding-top:12px;display:flex;justify-content:space-between;align-items:flex-start}
.total .l{font-size:9.5px;color:#5b6270}
.total .l small{display:block;font-size:7px;color:#b5bac3;margin-top:3px}
.total .v{font-size:17px;font-weight:700}
.btn.disabled{position:absolute;left:20px;right:20px;bottom:24px;background:#c9d1dc;color:#fff}
.ok{width:66px;height:66px;border-radius:50%;background:var(--green-soft);color:var(--green);margin:68px auto 0;display:flex;align-items:center;justify-content:center}
.ok svg{width:30px;height:30px;stroke-width:2.6}
.pick h3{text-align:center;font-size:17px;font-weight:800;margin-top:22px}
.pick p{text-align:center;font-size:9px;color:var(--muted);line-height:1.5;margin-top:10px}
.info-box{margin:26px 20px 0;background:var(--soft);border-radius:10px;padding:13px 14px 4px}
.info-box .kv{margin-bottom:10px}
.info-box .blue{color:var(--blue);font-weight:700}
.nav{position:absolute;left:0;right:0;bottom:0;height:58px;border-top:1px solid var(--line);display:flex;justify-content:space-around;align-items:center;padding:0 14px;color:#c2c7cf}
.nav svg{width:18px;height:18px}
.nav .act{color:var(--ink)}
.oi{margin:16px 18px 0;padding:16px 16px 10px}
.oi-row{display:flex;justify-content:space-between;margin-bottom:22px}
.oi-row .k{font-size:7.5px;font-weight:600;color:var(--muted);letter-spacing:.6px}
.oi-row .v{font-size:11.5px;font-weight:700;margin-top:6px}
.oi-row .r{text-align:right}
.code{display:inline-block;background:var(--soft);padding:3px 8px;border-radius:4px;font-size:10px}
.oi-line{display:flex;justify-content:space-between;font-size:9px;margin-top:8px}
.oi hr{border:none;border-top:1px solid var(--line);margin:-8px 0 14px}
.chat-hdr{height:84px;padding:42px 20px 0;display:flex;gap:14px;border-bottom:1px solid var(--line)}
.chat-hdr b{font-size:11.5px;font-weight:800}
.chat-hdr small{display:flex;align-items:center;gap:4px;font-size:7.5px;color:var(--green);margin-top:2px}
.chat-hdr small::before{content:"";width:5px;height:5px;border-radius:50%;background:var(--green)}
.chat{position:absolute;top:84px;left:0;right:0;bottom:0;background:var(--soft);padding:16px 14px}
.time{margin:0 auto;width:58px;text-align:center;font-size:7.5px;color:var(--muted);background:#e9ebef;border-radius:8px;padding:3px 0}
.msg{display:flex;align-items:flex-end;gap:8px;margin-top:16px}
.av{width:20px;height:20px;border-radius:50%;display:flex;align-items:center;justify-content:center;flex:none}
.av svg{width:11px;height:11px}
.bubble{font-size:9.5px;line-height:1.55;padding:10px 12px;border-radius:12px;background:#fff;border:1px solid var(--line)}
.msg.me .bubble{background:var(--blue);color:#fff;border:none;width:190px}
.composer{position:absolute;left:14px;right:14px;bottom:14px;display:flex;gap:8px}
.composer .in{flex:1;height:34px;border-radius:8px;background:#fff;border:1px solid var(--line);font-size:9px;color:#a3a9b4;display:flex;align-items:center;padding:0 10px}
.composer .send{width:34px;height:34px;border-radius:8px;background:var(--blue);color:#fff;display:flex;align-items:center;justify-content:center}
.hist{padding:14px 14px 12px;margin-bottom:12px}
.hist .top{display:flex;justify-content:space-between;align-items:center;font-size:10.5px;font-weight:800}
.tag{font-size:7.5px;font-weight:700;padding:3px 7px;border-radius:8px}
.tag.done{background:var(--green-soft);color:var(--green)}
.tag.date{background:var(--soft);color:#5b6270}
.hist .meta{font-size:7.5px;color:var(--muted);margin-top:8px}
.chips{display:flex;gap:6px;margin-top:14px}
.chip{width:22px;height:22px;border-radius:6px;background:var(--soft);display:flex;align-items:center;justify-content:center;font-size:8px;color:var(--muted);font-weight:600}
.chip svg{width:11px;height:11px;color:#5b6270}
</style>
</head>
<body>
<svg width="0" height="0" style="position:absolute">
  <defs>
    <symbol id="back" viewBox="0 0 24 24"><path d="M19 12H5M11 6l-6 6 6 6"/></symbol>
    <symbol id="search" viewBox="0 0 24 24"><circle cx="11" cy="11" r="7"/><path d="M20 20l-4-4"/></symbol>
    <symbol id="down" viewBox="0 0 24 24"><path d="M6 9l6 6 6-6"/></symbol>
    <symbol id="right" viewBox="0 0 24 24"><path d="M9 6l6 6-6 6"/></symbol>
    <symbol id="plus" viewBox="0 0 24 24"><path d="M12 5v14M5 12h14"/></symbol>
    <symbol id="minus" viewBox="0 0 24 24"><path d="M5 12h14"/></symbol>
    <symbol id="plusc" viewBox="0 0 24 24"><circle cx="12" cy="12" r="9"/><path d="M12 8v8M8 12h8"/></symbol>
    <symbol id="heart" viewBox="0 0 24 24"><path d="M12 20s-7-4.5-7-10a4 4 0 0 1 7-2.5A4 4 0 0 1 19 10c0 5.5-7 10-7 10z"/></symbol>
    <symbol id="doc" viewBox="0 0 24 24"><rect x="4" y="4" width="16" height="16" rx="2"/><path d="M8 9h8M8 13h8M8 17h5"/></symbol>
    <symbol id="thumb" viewBox="0 0 24 24"><path d="M7 10v10H4V10h3zM7 10l4-7a2 2 0 0 1 3 2l-1 4h6a2 2 0 0 1 2 2l-2 7a2 2 0 0 1-2 2H7"/></symbol>
    <symbol id="chat" viewBox="0 0 24 24"><path d="M4 19l1.5-4A8 8 0 1 1 9 19.5z"/></symbol>
    <symbol id="bag" viewBox="0 0 24 24"><rect x="4" y="7" width="16" height="13" rx="2"/><path d="M9 7V5a3 3 0 0 1 6 0v2M9 11a3 3 0 0 0 6 0"/></symbol>
    <symbol id="user" viewBox="0 0 24 24"><circle cx="12" cy="8" r="4"/><path d="M5 20a7 7 0 0 1 14 0"/></symbol>
    <symbol id="users" viewBox="0 0 24 24"><circle cx="9" cy="8" r="3.5"/><path d="M3 20a6 6 0 0 1 12 0M16 4.5a3.5 3.5 0 0 1 0 7M18 14a6 6 0 0 1 3 6"/></symbol>
    <symbol id="eye" viewBox="0 0 24 24"><path d="M2 12s4-7 10-7 10 7 10 7-4 7-10 7S2 12 2 12z"/><circle cx="12" cy="12" r="3"/></symbol>
    <symbol id="check" viewBox="0 0 24 24"><path d="M5 12l5 5 9-10"/></symbol>
    <symbol id="checkc" viewBox="0 0 24 24"><circle cx="12" cy="12" r="9"/><path d="M8 12l3 3 5-6"/></symbol>
    <symbol id="pin" viewBox="0 0 24 24"><path d="M12 21s-7-6.5-7-12a7 7 0 0 1 14 0c0 5.5-7 12-7 12z"/><circle cx="12" cy="9" r="2.5"/></symbol>
    <symbol id="navarrow" viewBox="0 0 24 24"><path d="M21 3L3 10l7 3 3 7z"/></symbol>
    <symbol id="share" viewBox="0 0 24 24"><circle cx="18" cy="5" r="2.5"/><circle cx="6" cy="12" r="2.5"/><circle cx="18" cy="19" r="2.5"/><path d="M8.2 10.8l7.6-4.4M8.2 13.2l7.6 4.4"/></symbol>
    <symbol id="lock" viewBox="0 0 24 24"><rect x="5" y="11" width="14" height="9" rx="2"/><path d="M8 11V8a4 4 0 0 1 8 0v3"/></symbol>
    <symbol id="arrow" viewBox="0 0 24 24"><path d="M5 12h14M13 6l6 6-6 6"/></symbol>
    <symbol id="star" viewBox="0 0 24 24"><path d="M12 3l2.7 5.6 6.1.9-4.4 4.3 1 6.1L12 17l-5.4 2.9 1-6.1L3.2 9.5l6.1-.9z"/></symbol>
    <symbol id="glasses" viewBox="0 0 24 24"><circle cx="6.5" cy="14" r="3.5"/><circle cx="17.5" cy="14" r="3.5"/><path d="M10 14h4M3 13l2-6M21 13l-2-6"/></symbol>
    <symbol id="slice" viewBox="0 0 24 24"><path d="M4 20L12 3l8 17z"/><path d="M6 16c4 2 8 2 12 0"/><circle cx="11" cy="11" r="1"/></symbol>
    <symbol id="bottle" viewBox="0 0 24 24"><path d="M10 3h4v4l2 3v11H8V10l2-3z"/><path d="M8 14h8"/></symbol>
    <symbol id="beer" viewBox="0 0 24 24"><path d="M5 6h11v15H5z"/><path d="M16 9h2a2 2 0 0 1 2 2v4a2 2 0 0 1-2 2h-2M8.5 10v7M12.5 10v7"/></symbol>
    <symbol id="cup" viewBox="0 0 24 24"><path d="M4 9h13v6a5 5 0 0 1-5 5H9a5 5 0 0 1-5-5z"/><path d="M17 11h1.5a2.5 2.5 0 0 1 0 5H17M8 3v3M12 3v3"/></symbol>
    <symbol id="home" viewBox="0 0 24 24"><path d="M4 11l8-7 8 7v9H4z"/><path d="M10 20v-5h4v5"/></symbol>
    <symbol id="compass" viewBox="0 0 24 24"><circle cx="12" cy="12" r="9"/><path d="M15.5 8.5l-2 5-5 2 2-5z"/></symbol>
    <symbol id="send" viewBox="0 0 24 24"><path d="M21 3L10 14M21 3l-7 18-4-7-7-4z"/></symbol>
    <symbol id="bot" viewBox="0 0 24 24"><rect x="5" y="8" width="14" height="11" rx="3"/><path d="M12 4v4M9 13h.01M15 13h.01"/></symbol>
    <symbol id="phone" viewBox="0 0 24 24"><rect x="7" y="3" width="10" height="18" rx="2"/><path d="M11 17h2"/></symbol>
    <symbol id="cake" viewBox="0 0 24 24"><path d="M4 20h16v-7H4zM4 16c2 1.5 4 1.5 6 0s4-1.5 6 0 3 1.5 4 0M8 13v-3M12 13v-3M16 13v-3M8 6v1M12 5v1M16 6v1"/></symbol>
  </defs>
</svg>

<h1 class="kit-title">Shop 24/7 Full UI Kit</h1>
<div class="kit-sub">USER JOURNEY &amp; SCREENS</div>

<div class="label c1 l1">01 - HOME</div>
<div class="label c2 l1">02 - LOGIN</div>
<div class="label c3 l1">03 - MERKLISTE</div>
<div class="label c4 l1">04 - NEWS</div>
<div class="label c1 l2">05 - STANDORT</div>
<div class="label c2 l2">06 - MENU</div>
<div class="label c3 l2">07 - MENU (OPEN)</div>
<div class="label c4 l2">08 - PRODUCT LIST</div>
<div class="label c1 l3">09 - DETAIL OVERLAY</div>
<div class="label c2 l3">10 - PAYMENT</div>
<div class="label c3 l3">11 - PICKUP</div>
<div class="label c4 l3">12 - ORDER INFO</div>
<div class="label c1 l4">13 - BESCHWERDE</div>
<div class="label c2 l4">14 - HISTORY</div>

<!-- 01 Home -->
<section class="screen c1 r1">
  <div class="home-logo" role="img" aria-label="Shop-Emblem in Gelb und Schwarz"></div>
  <div class="badge24">24h OPEN</div>
  <div class="home-sheet">
    <div class="handle"></div>
    <div class="home-name">SHOP 24/7</div>
    <div class="home-tag">SMART VENDING</div>
    <div class="btn blue" style="margin-top:26px"><svg class="i"><use href="#bag"/></svg>JETZT SHOPPEN</div>
    <div class="row-btn" style="margin-top:14px"><svg class="i" style="color:#8b93a1"><use href="#heart"/></svg>MERKLISTE<span class="sp"></span><svg class="i" style="width:10px;color:#c2c7cf"><use href="#right"/></svg></div>
    <div class="row-btn"><svg class="i" style="color:#8b93a1"><use href="#doc"/></svg>NEWS<span class="sp"></span><span class="dot"></span></div>
    <div style="display:flex;gap:8px">
      <div class="row-btn" style="flex:1;justify-content:center"><svg class="i" style="color:#8b93a1"><use href="#thumb"/></svg>LOB</div>
      <div class="row-btn" style="flex:1;justify-content:center"><svg class="i" style="color:#8b93a1"><use href="#chat"/></svg>CHAT</div>
    </div>
  </div>
  <div class="home-foot"><span>Login | Registrieren</span><span>Gast</span></div>
</section>

<!-- 02 Login -->
<section class="screen c2 r1">
  <div class="login">
    <div class="login-icon"><svg class="i"><use href="#user"/></svg></div>
    <h2>Willkommen</h2>
    <p>Bitte melden Sie sich an um<br>Punkte zu sammeln.</p>
    <div class="flabel">E-MAIL</div>
    <div class="input">name@beispiel.at</div>
    <div class="flabel" style="margin-top:16px">PASSWORT</div>
    <div class="input"><span style="letter-spacing:2px;color:#5b6270">••••••••</span><svg class="i"><use href="#eye"/></svg></div>
    <div class="forgot">Passwort vergessen?</div>
    <div class="btn blue">LOGIN</div>
    <div class="oder">ODER</div>
    <div class="btn outline">KONTO ERSTELLEN</div>
  </div>
</section>

<!-- 03 Merkliste -->
<section class="screen c3 r1">
  <div class="hdr"><svg class="i"><use href="#back"/></svg>MERKLISTE</div>
  <div class="body-gray">
    <div class="card item">
      <div class="ph" role="img" aria-label="Foto einer Pizza Margherita"></div>
      <div class="info"><div class="name">MARGHERITA</div><span class="pts">40 PTS</span>
        <div class="desc">Klassische Pizza mit Tomatensauce und Mozzarella.</div>
        <div class="bp">1 EUR = 1 Fachpunkt</div><span class="add"><svg class="i"><use href="#plusc"/></svg></span></div>
    </div>
    <div class="card item">
      <div class="ph" role="img" aria-label="Foto einer Salami-Pizza"></div>
      <div class="info"><div class="name">SALAMI</div><span class="pts">45 PTS</span>
        <div class="desc">Der Klassiker mit würziger Salami.</div>
        <div class="bp">1 EUR = 1 Fachpunkt</div><span class="add"><svg class="i"><use href="#plusc"/></svg></span></div>
    </div>
    <div class="card item">
      <div class="ph" role="img" aria-label="Foto einer Pizza Diavolo"></div>
      <div class="info"><div class="name">DIAVOLO</div><span class="pts">50 PTS</span>
        <div class="desc">Scharf mit Paprika und Pfefferoni.</div>
        <div class="bp">1 EUR = 1 Fachpunkt</div><span class="add"><svg class="i"><use href="#plusc"/></svg></span></div>
    </div>
  </div>
</section>

<!-- 04 News -->
<section class="screen c4 r1">
  <div class="hdr"><svg class="i"><use href="#back"/></svg>NEWS</div>
  <div style="padding:16px 14px">
    <div class="card news"><div class="nicon" style="background:var(--navy);color:var(--yellow)"><svg class="i"><use href="#phone"/></svg></div>
      <div><h4>DIE NEUE APP IST DA</h4><p>Ab sofort Punkte sammeln und Prämien freischalten! Dein alter Stempelpass geht nicht verloren.</p></div></div>
    <div class="card news"><div class="nicon" style="background:var(--yellow);color:var(--ink)"><svg class="i"><use href="#cake"/></svg></div>
      <div><h4>GEBURTSTAG +50 PTS</h4><p>Wir laden dich zu einer Geburtstagspizza ein. Einfach am Standort deine Punkte einlösen.</p></div></div>
    <div class="card news"><div class="nicon" style="background:var(--blue-soft);color:var(--blue)"><svg class="i"><use href="#users"/></svg></div>
      <div><h4>FREUNDE EINLADEN</h4><p>Lade jetzt deine Freunde zur Shop App ein und hol dir 5 Extrapunkte für jeden.</p></div></div>
  </div>
</section>

<!-- 05 Standort -->
<section class="screen c1 r2">
  <div class="hdr"><svg class="i"><use href="#back"/></svg>STANDORT</div>
  <div class="map" role="img" aria-label="Stadtplan rund um den Automatenstandort">
    <div class="pill" style="left:18px;top:38px"><svg class="i" style="width:9px;height:9px;color:var(--blue)"><use href="#navarrow"/></svg>1.2 km entfernt</div>
    <div class="pill" style="left:76px;top:200px">Leoben, Murgasse 14</div>
    <div class="map-pin"><svg class="i"><use href="#pin"/></svg></div>
  </div>
  <div class="loc-card">
    <div class="kv">Automatennummer<b>A1</b></div>
    <div class="kv">Fach Nummer<b>910</b></div>
    <div class="kv">Status<span class="on">● Online</span></div>
    <div class="btn navy" style="height:34px;font-size:10px"><svg class="i" style="width:11px"><use href="#share"/></svg>TEILEN</div>
  </div>
</section>

<!-- 06 Menu -->
<section class="screen c2 r2">
  <div class="hdr center" style="border:none"><svg class="i"><use href="#back"/></svg><span class="t">MENÜ</span><svg class="i"><use href="#search"/></svg></div>
  <div class="mrow"><svg class="i"><use href="#slice"/></svg>Pizza &amp; Snacks<span class="sp"></span><svg class="i" style="width:11px;color:#c2c7cf"><use href="#down"/></svg></div>
  <div class="mrow active"><svg class="i"><use href="#glasses"/></svg>Kontaktlinsen<span class="sp"></span><svg class="i" style="width:11px"><use href="#right"/></svg></div>
  <div class="mrow"><svg class="i"><use href="#bottle"/></svg>Getränke<span class="sp"></span><svg class="i" style="width:11px;color:#c2c7cf"><use href="#down"/></svg></div>
  <div class="mrow"><svg class="i"><use href="#beer"/></svg>Bier<span class="sp"></span><svg class="i" style="width:11px;color:#c2c7cf"><use href="#down"/></svg></div>
  <div class="mrow"><svg class="i"><use href="#cup"/></svg>Kaffee &amp; Tee<span class="sp"></span><svg class="i" style="width:11px;color:#c2c7cf"><use href="#down"/></svg></div>
</section>

<!-- 07 Menu open -->
<section class="screen c3 r2" style="background:var(--soft)">
  <div class="hdr center" style="border:none"><svg class="i"><use href="#back"/></svg><span class="t">KONTAKTLINSEN</span><svg class="i"><use href="#search"/></svg></div>
  <div class="dbar"><svg class="i"><use href="#glasses"/></svg>-3.0 Dioptrien<span class="sp"></span><svg class="i" style="width:12px"><use href="#down"/></svg></div>
  <div style="padding-top:4px">
    <div class="dopt">- 0.5 Dioptrien</div>
    <div class="dopt">- 1.0 Dioptrien</div>
    <div class="dopt">- 1.5 Dioptrien</div>
    <div class="dopt">- 2.0 Dioptrien</div>
    <div class="dopt sel">- 3.0 Dioptrien<svg class="i" style="width:12px"><use href="#checkc"/></svg></div>
  </div>
  <div class="soft-btn">ZUBEHÖR ANZEIGEN</div>
</section>

<!-- 08 Product list -->
<section class="screen c4 r2" style="background:var(--soft)">
  <div class="dark-top">
    <div class="row"><svg class="i"><use href="#back"/></svg>GETRÄNKE<svg class="i"><use href="#search"/></svg></div>
    <div class="select"><svg class="i y" style="width:12px"><use href="#beer"/></svg>BIER<span class="sp"></span><svg class="i" style="width:10px;color:#8b93a1"><use href="#down"/></svg></div>
  </div>
  <div class="card prod" style="margin-top:14px">
    <div class="ph" role="img" aria-label="Foto einer Bierdose mit Glas"></div>
    <div><div class="nm">ALMTALER MÄRZEN</div><div class="sb">0,5l Dose • Hell</div><div class="pr">1,99 €</div></div>
    <span class="star"><svg class="i"><use href="#star"/></svg></span><span class="plus"><svg class="i"><use href="#plus"/></svg></span>
  </div>
  <div class="card prod">
    <div class="ph" role="img" aria-label="Foto einer Bierflasche"></div>
    <div><div class="nm">VELLANO BIRRA</div><div class="sb">0,33l Dose</div><div class="pr">2,49 € <i>Info</i></div></div>
    <span class="star"><svg class="i"><use href="#star"/></svg></span><span class="plus"><svg class="i"><use href="#plus"/></svg></span>
  </div>
  <div class="btn blue" style="position:absolute;left:14px;right:14px;bottom:22px;height:36px;font-size:10px;font-weight:600">In den Warenkorb (59,94 €)</div>
</section>

<!-- 09 Detail -->
<section class="screen c1 r3">
  <div class="dt-top"></div>
  <div class="dt-sheet">
    <div class="handle"></div>
    <div class="dt-head">
      <div class="ph" role="img" aria-label="Foto eines Glases Märzenbier"></div>
      <div><h3>ALMTALER MÄRZEN</h3><div class="sb">0,5l Dose</div><div class="nw">Nährwerte</div><div class="pr">1,99 €</div></div>
    </div>
    <div class="stepper"><span class="b"><svg class="i" style="width:11px"><use href="#minus"/></svg></span>1<span class="b"><svg class="i" style="width:11px"><use href="#plus"/></svg></span></div>
    <div class="opt on" style="margin-top:24px"><span class="radio on"></span>Einzeldose</div>
    <div class="opt"><span class="radio"></span>6er Träger<span class="sp"></span><small>+9,95 €</small></div>
    <div class="btn blue" style="margin-top:26px">Weiter (Gesamt 1,99 €)<svg class="i" style="width:12px"><use href="#arrow"/></svg></div>
  </div>
</section>

<!-- 10 Payment -->
<section class="screen c2 r3">
  <div class="pay-top"><svg class="i"><use href="#back"/></svg>BEZAHLUNG</div>
  <div class="pay-body">
    <h5>ZAHLUNGSMETHODE</h5>
    <div class="popt on"><span class="radio on"></span>Zahlio<span class="sp"></span></div>
    <div class="popt"><span class="radio"></span>Kreditkarte<span class="sp"></span></div>
    <div class="popt"><span class="radio"></span>Fokusgruppe<span class="sp"></span><span class="free">FREE</span></div>
  </div>
  <div class="total"><div class="l">Gesamtbetrag<small>Inkl. MwSt.</small></div><div class="v">59,94 €</div></div>
  <div class="btn disabled"><svg class="i" style="width:11px"><use href="#lock"/></svg>Kostenpflichtig bestellen</div>
</section>

<!-- 11 Pickup -->
<section class="screen c3 r3 pick">
  <div class="hdr center"><svg class="i"><use href="#back"/></svg><span class="t">VERLAUF</span><svg class="i"><use href="#search"/></svg></div>
  <div class="ok"><svg class="i"><use href="#check"/></svg></div>
  <h3>Abholbereit!</h3>
  <p>Deine Bestellung steht im<br>Showroom zur Abholung bereit.</p>
  <div class="info-box">
    <div class="kv">Ort<b>Showroom</b></div>
    <div class="kv">Status<span class="blue">Offene Abholung</span></div>
  </div>
  <div class="btn navy" style="margin:20px 20px 0;height:46px">JETZT AUSGEBEN</div>
  <div class="nav"><svg class="i"><use href="#home"/></svg><svg class="i"><use href="#compass"/></svg><svg class="i"><use href="#pin"/></svg><svg class="i act"><use href="#user"/></svg></div>
</section>

<!-- 12 Order info -->
<section class="screen c4 r3">
  <div class="hdr"><svg class="i"><use href="#back"/></svg>BESTELLINFO</div>
  <div class="card oi">
    <div class="oi-row"><div><div class="k">BESTELLT UM</div><div class="v">14:30 Uhr</div></div><div class="r"><div class="k">STATUS</div><div class="v" style="color:var(--green)">Bezahlt</div></div></div>
    <div class="oi-row"><div><div class="k">VORBESTELLT FÜR</div><div class="v">Sofort</div></div><div class="r"><div class="k">ABHOLCODE</div><div class="v"><span class="code">#8X92</span></div></div></div>
    <hr>
    <div class="k" style="font-size:7.5px;font-weight:600;color:var(--muted);letter-spacing:.6px">PRODUKTE</div>
    <div class="oi-line"><span>1x Almtaler Märzen 0.5l</span><span>1,99 €</span></div>
    <div class="oi-line" style="margin-bottom:10px"><span>1x Vellano Birra 0.33l</span><span>2,49 €</span></div>
  </div>
  <div class="btn blue" style="margin:18px 18px 0;font-size:10px">ABHOLINFO ANZEIGEN</div>
  <div class="btn outline" style="margin:10px 18px 0;font-size:9.5px;color:#5b6270">RECHNUNG SENDEN</div>
</section>

<!-- 13 Chat -->
<section class="screen c1 r4">
  <div class="chat-hdr"><svg class="i" style="margin-top:6px"><use href="#back"/></svg><div><b>Support Chat</b><small>Online</small></div></div>
  <div class="chat">
    <div class="time">Heute 10:23</div>
    <div class="msg"><span class="av" style="background:#e6e8ec;color:#5b6270"><svg class="i"><use href="#bot"/></svg></span><div class="bubble">Hallo! Wie können wir dir helfen?</div></div>
    <div class="msg me"><div class="bubble">Mein Produkt wurde nicht ausgegeben.</div><span class="av" style="background:var(--blue-soft);color:var(--blue)"><svg class="i"><use href="#user"/></svg></span></div>
    <div class="composer"><div class="in">Nachricht schreiben...</div><div class="send"><svg class="i"><use href="#send"/></svg></div></div>
  </div>
</section>

<!-- 14 History -->
<section class="screen c2 r4">
  <div class="hdr"><svg class="i"><use href="#back"/></svg>LETZTE BESTELLUNGEN</div>
  <div style="padding:14px 14px">
    <div class="card hist">
      <div class="top">#8X92<span class="tag done">Erledigt</span></div>
      <div class="meta">Heute, 14:30 Uhr • 2 Artikel</div>
      <div class="chips"><span class="chip"><svg class="i"><use href="#beer"/></svg></span><span class="chip">+1</span></div>
    </div>
    <div class="card hist">
      <div class="top">#A72B<span class="tag date">20. Okt</span></div>
      <div class="meta">1 Artikel</div>
      <div class="chips"><span class="chip"><svg class="i"><use href="#slice"/></svg></span></div>
    </div>
  </div>
</section>
</body>
</html>
```